Banner Design Project

I need a banner designed that will be used in an outdoor location. The banner is 8' x 3' and can be full color.

This is a general advertising banner for a photography business; I can provide images if needed;

My website is: www.marklowdenphotostudio.com

It will be used at the following school: http://www.rbta.net/

Target Market(s)

All ages but should appeal to High School Students

Industry/Entity Type

Advertising

Requirements
Must have
• Integrate Logo

```html
<!DOCTYPE html>
<html lang="en">
<head>
<meta charset="utf-8">
<title>Mark Lowden Photo Studio — 8 × 3 ft Banner</title>
<link rel="stylesheet" href="https://fonts.googleapis.com/css2?family=Open+Sans:wght@600;700&display=swap">
<style>
  :root {
    --page: #ffffff;
    --dimension-ink: #9a9b9d;
    --dimension-line: #c4c5c7;
    --silver-edge: #b2b3b5;
    --silver-mid: #dcdddf;
    --silver-light: #f5f5f5;
    --sky-band: #72b9e6;
    --brand-navy: #0a4b8c;
    --url-grey: #55565a;
  }
  * { margin: 0; padding: 0; box-sizing: border-box; }
  html, body {
    width: 1200px;
    height: 478px;
    overflow: hidden;
    background: var(--page);
    font-family: "Open Sans", Arial, sans-serif;
  }
  .sheet {
    position: relative;
    width: 1200px;
    height: 478px;
  }
  .dimension {
    position: absolute;
    color: var(--dimension-ink);
    font-weight: 700;
    font-size: 20px;
    letter-spacing: 0.04em;
    line-height: 1;
  }
  .dimension--width {
    left: 48px;
    right: 0;
    top: 8px;
    display: flex;
    align-items: center;
    gap: 22px;
  }
  .dimension--height {
    left: 8px;
    top: 44px;
    bottom: 1px;
    width: 22px;
    display: flex;
    flex-direction: column;
    align-items: center;
    gap: 18px;
  }
  .dimension__rule {
    flex: 1;
    background: var(--dimension-line);
  }
  .dimension--width .dimension__rule { height: 2px; }
  .dimension--height .dimension__rule { width: 2px; }
  .dimension--height .dimension__label {
    writing-mode: vertical-rl;
    transform: rotate(180deg);
  }
  .banner {
    position: absolute;
    left: 48px;
    top: 44px;
    width: 1152px;
    height: 434px;
    display: flex;
    flex-direction: column;
  }
  .banner__hero {
    height: 317px;
    background: linear-gradient(90deg, var(--silver-edge) 0%, var(--silver-mid) 22%, var(--silver-light) 50%, var(--silver-mid) 78%, var(--silver-edge) 100%);
    display: flex;
    align-items: center;
    justify-content: center;
  }
  .brand-name {
    color: var(--brand-navy);
    font-weight: 700;
    font-size: 50px;
    letter-spacing: 0.16em;
    white-space: nowrap;
    margin-top: 6px;
  }
  .banner__footer {
    flex: 1;
    background: var(--sky-band);
    display: flex;
    align-items: center;
    justify-content: center;
  }
  .website {
    color: var(--url-grey);
    font-weight: 700;
    font-size: 41px;
    letter-spacing: 0.005em;
    margin-top: 12px;
  }
</style>
</head>
<body>
  <main class="sheet">
    <div class="dimension dimension--width">
      <span class="dimension__rule"></span>
      <span class="dimension__label">8 FEET</span>
      <span class="dimension__rule"></span>
    </div>
    <div class="dimension dimension--height">
      <span class="dimension__rule"></span>
      <span class="dimension__label">3 FEET</span>
      <span class="dimension__rule"></span>
    </div>

    <section class="banner">
      <div class="banner__hero">
        <h1 class="brand-name">MARK LOWDEN PHOTO STUDIO</h1>
      </div>
      <footer class="banner__footer">
        <p class="website">www.marklowdenphotostudio.com</p>
      </footer>
    </section>
  </main>
</body>
</html>
```